Linden Medical - Flyer

We are a full service pharmacy that specializes in diabetic testing and medications. We research the patient's insurance to maximize their insurance benefit and then deliver the medications monthly directly to the patient's doorstep, for free! We save the patient, time and money every month.
We would love a flyer that we can distribute to Doctor's offices and patients that sum up our pharmacy. Emphasis on saving money, time, and getting the best quality supplies by maximizing their insurance. We want it to be eye catching, clean, and professional.
You can use our logo or feel free to make your own design.
Updates
Target Market(s)
diabetic patients wanting to save money
Industry/Entity Type
Insurance
Look and feel
Each slider illustrates characteristics of the customer's brand and the style your logo design should communicate.

```html
<!DOCTYPE html>
<html lang="en">
<head>
<meta charset="utf-8">
<title>Linden Medical – Flyer</title>
<link rel="stylesheet" href="https://fonts.googleapis.com/css2?family=Arimo:wght@400;700&display=swap">
<style>
  :root {
    --page-bg: #eef1f3;
    --sky-top: #cfeef4;
    --sky-mid: #f4fbfd;
    --sky-low: #e2f3f8;
    --navy: #1c2a5c;
    --red: #c8102e;
    --green: #7cbd2a;
    --green-light: #b7dc7c;
    --green-dark: #5e9e1c;
    --teal: #1f5a67;
    --ink: #1e1e1e;
    --grey: #7a7a7a;
    --white: #ffffff;
  }
  * { box-sizing: border-box; margin: 0; padding: 0; }
  html, body {
    width: 1200px; height: 1019px; overflow: hidden;
    background: var(--page-bg);
    font-family: "Arimo", Arial, sans-serif;
  }
  .sheet {
    position: absolute; top: 179px; width: 528px; height: 682px;
    overflow: hidden;
    background: radial-gradient(ellipse at 30% 20%, var(--sky-mid) 0%, var(--sky-low) 55%, var(--sky-top) 100%);
    box-shadow: 0 6px 18px rgba(0,0,0,.18);
  }
  .sheet--front { left: 57px; }
  .sheet--back { left: 613px; }
  .abs { position: absolute; }
  .placeholder { position: absolute; border-radius: 8px; }

  .wordmark {
    position: absolute; display: flex; align-items: center; gap: 10px;
    color: var(--grey); font-weight: 400; letter-spacing: 1px;
  }
  .wordmark__dot { background: var(--green); border-radius: 50%; flex: none; }

  .headline {
    position: absolute; left: 0; width: 528px; text-align: center;
    color: var(--navy); font-weight: 700; font-size: 17px; line-height: 28px;
    top: 134px; text-transform: uppercase;
  }
  .headline em { font-style: normal; color: var(--red); }
  .headline .big { font-size: 23px; }

  .benefit { position: absolute; top: 369px; width: 130px; text-align: center; }
  .benefit__circle {
    width: 68px; height: 68px; border-radius: 50%; margin: 0 auto;
    background: var(--green); display: flex; align-items: center; justify-content: center;
  }
  .benefit__art { width: 42px; height: 42px; border-radius: 50%; background: radial-gradient(#f2e6c8, #c28a3e); }
  .benefit__label { margin-top: 13px; font-size: 12.5px; color: var(--ink); }

  .call-badge {
    position: absolute; left: 298px; top: 469px; width: 154px; height: 154px;
    border-radius: 50%; background: var(--red); color: var(--white); text-align: center;
  }
  .call-badge__label { position: absolute; top: 22px; left: 48px; font-size: 12px; font-weight: 700; line-height: 15px; text-align: center; }
  .call-badge__icon { position: absolute; left: 28px; top: 22px; }
  .call-badge__number { position: absolute; top: 74px; width: 100%; font-size: 25px; font-weight: 700; }

  .site { position: absolute; color: var(--white); font-size: 17px; }

  .copy { position: absolute; left: 26px; top: 22px; width: 470px; color: var(--ink); font-size: 16.5px; line-height: 22px; }
  .copy p { margin-bottom: 24px; }
  .cta { position: absolute; left: 26px; top: 298px; }
  .cta__title { color: var(--red); font-size: 26px; font-weight: 700; }
  .cta__text { font-size: 16px; line-height: 21px; color: var(--ink); margin-top: 2px; }

  .ribbon { position: absolute; color: var(--white); background: var(--teal); display: flex; align-items: center; justify-content: center; }
  .ribbon::after { content: ""; position: absolute; inset: 3px 0 3px 3px; border: 1px dashed rgba(255,255,255,.6); border-right: none; }
  .ribbon--amount { left: 418px; top: 346px; width: 110px; height: 39px; font-size: 29px; font-weight: 700; }
  .ribbon--gift { left: 311px; top: 389px; width: 217px; height: 46px; font-size: 23px; }
  .ribbon--order { left: 251px; top: 437px; width: 277px; height: 44px; font-size: 23px; padding-left: 50px;
    clip-path: polygon(0 0, 100% 0, 100% 100%, 0 100%, 28px 50%); }
  .ribbon--order::after { left: 30px; }

  .tollfree { position: absolute; left: 0; width: 100%; padding-left: 88px; top: 640px; text-align: center; color: var(--white); font-size: 25px; font-weight: 700; }
</style>
</head>
<body>

<section class="sheet sheet--front" aria-label="Flyer front">
  <svg class="abs" width="528" height="682" viewBox="0 0 528 682" style="left:0;top:0">
    <path d="M0 560 C 170 610, 380 520, 528 448 L528 682 L0 682 Z" fill="var(--green-light)"/>
    <path d="M0 590 C 170 640, 380 560, 528 470 L528 682 L0 682 Z" fill="var(--green)"/>
  </svg>

  <div class="wordmark" style="left:132px;top:38px;font-size:38px;">
    <span class="wordmark__dot" style="width:26px;height:26px"></span>Linden Medical
  </div>

  <h1 class="headline">Are the <em>costs</em> of your diabetic testing s<br>upplies as high as your <em class="big">blood sugar?</em></h1>

  <div class="placeholder" role="img" aria-label="Heartbeat line with a red heart held by a green hand"
       style="left:118px;top:202px;width:300px;height:160px;background:radial-gradient(circle at 50% 45%, #e34a4a 0 14%, #bfe8ee 15%, rgba(207,238,244,0) 70%);"></div>

  <div class="benefit" style="left:12px">
    <div class="benefit__circle"><div class="benefit__art" role="img" aria-label="Compass meter icon"></div></div>
    <div class="benefit__label">FREE METER</div>
  </div>
  <div class="benefit" style="left:133px">
    <div class="benefit__circle"><div class="benefit__art" role="img" aria-label="Wallet icon"></div></div>
    <div class="benefit__label">SAVE MONEY</div>
  </div>
  <div class="benefit" style="left:257px">
    <div class="benefit__circle"><div class="benefit__art" role="img" aria-label="Alarm clock icon"></div></div>
    <div class="benefit__label">SAVE TIME</div>
  </div>
  <div class="benefit" style="left:387px">
    <div class="benefit__circle"><div class="benefit__art" role="img" aria-label="Delivery briefcase icon"></div></div>
    <div class="benefit__label">FREE DELIVERY</div>
  </div>

  <div class="placeholder" role="img" aria-label="Photo of four fingertips drawn as a smiling family"
       style="left:42px;top:474px;width:232px;height:143px;background:linear-gradient(180deg,#f0c7b0,#d99c80);"></div>

  <div class="call-badge">
    <svg class="call-badge__icon" width="22" height="30" viewBox="0 0 22 30">
      <path d="M5 2 C1 4,0 10,3 17 C6 24,11 28,16 28 L19 24 L14 19 L11 21 C8 18,7 14,7 11 L10 9 L8 2 Z" fill="var(--white)"/>
    </svg>
    <div class="call-badge__label">Toll Free<br>Number</div>
    <div class="call-badge__number">13572468</div>
  </div>

  <div class="site" style="left:146px;top:646px;">www.lindenmedical.com</div>
</section>

<section class="sheet sheet--back" aria-label="Flyer back">
  <svg class="abs" width="528" height="682" viewBox="0 0 528 682" style="left:0;top:0">
    <path d="M0 480 C 120 600, 330 640, 528 560 L528 682 L0 682 Z" fill="var(--green-light)"/>
    <path d="M0 585 C 150 605, 380 610, 528 590 L528 682 L0 682 Z" fill="var(--green)"/>
  </svg>

  <div class="copy">
    <p>We are a full service pharmacy that specializes in diabetic testing supplies and oral medications.</p>
    <p>We research your insurance to determine how to save you the most money</p>
    <p>We then contact your physician to get the appropriate authorization</p>
    <p>We ship your testing supplies and oral medications directly to your home for free!</p>
  </div>

  <div class="cta">
    <div class="cta__title">Get started Today!</div>
    <div class="cta__text">Call our toll free number OR<br>go to our website and fill our form.</div>
  </div>

  <div class="ribbon ribbon--amount">$20</div>
  <div class="ribbon ribbon--gift">Gift Card is given</div>
  <div class="ribbon ribbon--order">your first order</div>

  <div class="placeholder" role="img" aria-label="Photo of a businessman seen from behind with arms raised"
       style="left:75px;top:411px;width:177px;height:199px;background:linear-gradient(180deg,#3b3f44,#1c1f22);opacity:.85;"></div>

  <div class="wordmark" style="left:300px;top:524px;font-size:24px;">
    <span class="wordmark__dot" style="width:18px;height:18px"></span>Linden Medical
  </div>
  <div class="abs" style="left:286px;top:576px;font-size:15px;color:var(--teal);">www.lindenmedical.com</div>

  <div class="placeholder" role="img" aria-label="Red heart held by a green hand"
       style="left:8px;top:579px;width:80px;height:75px;border-radius:50%;background:radial-gradient(circle at 50% 40%,#e0303a 0 45%,#6cbf2c 46% 70%,rgba(0,0,0,0) 71%);"></div>

  <div class="tollfree">Toll Free Number 13572468</div>
</section>

</body>
</html>
```